Business Card Design and a letter head logo

50/50 share milker dairy farmer of 400 cows with a silage and haymaking sideline business
15 years farming currently looking for new opportunities within the dairy farming sector. trying to put together a portfolio to get another 50/50 share milking job aswell

Industry/Entity Type

Farming

Contact Information for Business Card

Brindle Farming LTD
Corwin & Lisette Pargeter
263 Kellow Ridge Highway
RD4 Tepuhina 0382
Whangarei
pargeter.corwin@fernmail.example.nz
0274381926
(09) 5817342

```html
<!DOCTYPE html>
<html lang="en">
<head>
<meta charset="utf-8">
<title>Brindle Farming LTD – Business Card</title>
<link rel="stylesheet" href="https://fonts.googleapis.com/css2?family=Saira+Condensed:ital,wght@0,300;0,400;0,700;1,400&display=swap">
<style>
  :root {
    --page-bg: #e6e4df;
    --card-bg: #ffffff;
    --ink: #1c1c1c;
    --ink-soft: #2e2e2e;
    --card-shadow: rgba(0, 0, 0, 0.18);
  }
  html, body {
    margin: 0;
    padding: 0;
    width: 1200px;
    height: 892px;
    overflow: hidden;
    background: var(--page-bg);
  }
  .business-card {
    position: absolute;
    left: 100px;
    top: 160px;
    width: 1000px;
    height: 572px;
    background: var(--card-bg);
    box-shadow: 0 6px 24px var(--card-shadow);
    font-family: "Saira Condensed", sans-serif;
    color: var(--ink);
  }
  .brand-name {
    position: absolute;
    left: 150px;
    top: 78px;
    margin: 0;
    font-size: 68px;
    font-weight: 700;
    letter-spacing: 1px;
    line-height: 1;
    color: var(--ink);
  }
  .owner-block {
    position: absolute;
    left: 130px;
    top: 190px;
  }
  .owner-names {
    margin: 0;
    font-size: 50px;
    font-weight: 300;
    letter-spacing: 1px;
    line-height: 1;
  }
  .owner-role {
    margin: 2px 0 0 -4px;
    font-size: 20px;
    font-style: italic;
    font-weight: 400;
    letter-spacing: 1.5px;
  }
  .contact-list {
    position: absolute;
    left: 96px;
    top: 330px;
    margin: 0;
    padding: 0;
    list-style: none;
    font-size: 26px;
    font-weight: 400;
    color: var(--ink-soft);
    line-height: 1.42;
  }
  .contact-list .phone-mobile { padding-left: 10px; }
  .contact-list .phone-landline { padding-left: 4px; }
  .contact-list .email { padding-left: 0; font-size: 24px; }
  .contact-list .address { margin-left: -6px; }
</style>
</head>
<body>
  <article class="business-card">
    <h1 class="brand-name">Brindle Farming LTD</h1>
    <div class="owner-block">
      <p class="owner-names">Corwin &amp; Lisette Pargeter</p>
      <p class="owner-role">owner</p>
    </div>
    <ul class="contact-list">
      <li class="phone-mobile">0274381926</li>
      <li class="phone-landline">(09) 5817342</li>
      <li class="email">pargeter.corwin@fernmail.example.nz</li>
      <li class="address">263 Kellow Ridge Highway RD4 Tepuhina 0382 Whangarei</li>
    </ul>
  </article>
</body>
</html>
```